Orchard Bough Growing - Book Covers - Ebook, Paperback, Hardcover

Title would be:
Orchard Bough Growing
Subtitle: 7 Easy Stages Covering, Ground Choice, Blossom Care and Feeding, Trimming, Tiny Plots, Bug Management, Exotic Orchard Plants, and Vines
Author: Marlene Okafor
I would like the designer to have a couple of beautiful pictures on the cover. Please make it unique.
This would be posted on Quillora so please use specifications for book covers on Quillora
Back Cover should read:
Orchard Bough Growing
7 Easy Stages Covering, Ground Choice, Blossom Care and Feeding, Trimming, Tiny Plots, Bug Management, Exotic Orchard Plants, and Vines
Marlene Okafor
How to grow a thriving orchard and reap a bountiful harvest in less than a year – in both urban and non-urban settings
Fruit trees are fun to grow and will reward you with years of fresh, juicy homegrown produce.
However, the process can be excruciating, especially if you don’t know the best varieties to grow or how to control pests and diseases.
With a little planning and guidance, you will soon be biting into mellow fruits from trees in your backyard – including cherries, plums, pears, apples, and more.
All you need is to learn how to care for the trees, which you will find inside.
In Orchard Bough Growing, you’ll discover:
● How to pick the right fruit tree varieties for your growing zone and needs to ensure the plants don’t die
● How to effectively plan and prepare the planting site to lay a good foundation for your incoming trees
● How to choose the right irrigation system for your orchard and keep your fruit trees nourished all year long
● Examples of fruit garden plans for different regions – including a guide to help you design your small backyard space
● How to plant fruits to ensure proper pollination, fertilization, and flourishing growth of your produce
● Different fruit tree propagation methods with step-by-step instructions to help you grow your trees without spending money on costly grafts
● When and how to harvest fruits to ensure you collect them at their best and prevent wasting your hard work
● How to boost fruit production, encourage growth, and protect your trees from dangerous diseases
● How to look after fruit trees during all seasons, practice organic farming, and control pests in your garden
And much more…
It’s time to grow your mini-orchard and bask in years of harvest and sweetness from your labor.
Discover how you can have a thriving orchard and a bountiful fruit harvest.
Updates
Hello all Designers,
Please include this on the back cover as I forgot to include it in my main project:
Back Cover to read:
Orchard Bough Growing
Marlene Okafor
And much more…
Target Market(s)
People Who Love Gardening
Industry/Entity Type
Publishing
Requirements
Must have
- Title, Subtitle, Author Name, Beautiful Design, Eye Catching making you want to buy the book
Nice to have
- Large title, Easy to read subtitle intriguing pictures
Should not have
- Busy with too much stuff going on

```html
<!DOCTYPE html>
<html lang="en">
<head>
<meta charset="utf-8">
<title>Orchard Bough Growing – Cover Wrap</title>
<link href="https://fonts.googleapis.com/css2?family=Great+Vibes&family=Montserrat:wght@800;900&family=Roboto:wght@400;500;700&family=Roboto+Condensed:ital,wght@1,700&display=swap" rel="stylesheet">
<style>
  :root {
    --paper: #ffffff;
    --stage: #ffffff;
    --ink: #1c1c1c;
    --leaf: #17a33a;
    --berry: #f2210c;
    --canopy-dark: #3e6a1c;
    --canopy-light: #7fa83a;
    --fruit-warm: #c98a2c;
  }
  * { margin: 0; padding: 0; box-sizing: border-box; }
  html, body { width: 1200px; height: 343px; overflow: hidden; background: var(--stage); }
  .canvas { position: relative; width: 1200px; height: 343px; background: var(--stage); overflow: hidden; }

  .wrap {
    position: absolute; left: 346px; top: 0;
    width: 512px; height: 343px; background: var(--paper);
    font-family: "Roboto", sans-serif; color: var(--ink);
  }
  .script { font-family: "Great Vibes", cursive; color: var(--berry); line-height: 1.3; white-space: nowrap; }
  .block-title { font-family: "Montserrat", sans-serif; font-weight: 900; color: var(--leaf); white-space: nowrap; line-height: 1; }
  .author { font-family: "Montserrat", sans-serif; font-weight: 900; color: var(--berry); white-space: nowrap; line-height: 1; }

  /* Back cover */
  .back { position: absolute; left: 0; top: 0; width: 226px; height: 343px; }
  .back .script { position: absolute; left: 0; width: 226px; text-align: center; top: 8px; font-size: 28px; }
  .back .block-title { position: absolute; left: 0; width: 226px; text-align: center; top: 49px; font-size: 11px; letter-spacing: 0.9px; }
  .back .byline { position: absolute; left: 0; width: 226px; text-align: center; top: 63px; font-weight: 700; font-size: 6.6px; color: var(--berry); }
  .back .blurb { position: absolute; left: 11px; top: 74px; width: 206px; font-size: 4.7px; line-height: 6.85px; font-weight: 500; text-align: justify; text-align-last: center; }
  .back .discover-head { position: absolute; left: 0; width: 226px; text-align: center; top: 130.5px; font-size: 4.5px; font-weight: 500; }
  .back .points { position: absolute; top: 139px; list-style: none; font-size: 4.7px; line-height: 6.9px; font-weight: 500; }
  .back .points li { position: relative; padding-left: 5px; margin-bottom: 6.9px; }
  .back .points li::before { content: ""; position: absolute; left: 0; top: 2.4px; width: 2.2px; height: 2.2px; border-radius: 50%; background: var(--ink); }
  .back .points li.tail { margin-top: -6.9px; }
  .back .points li.tail::before { display: none; }
  .back .points.col-a { left: 11px; width: 98px; }
  .back .points.col-b { left: 116px; width: 101px; }
  .back .closing { position: absolute; left: 16px; width: 196px; top: 285px; text-align: center; font-family: "Roboto Condensed", sans-serif; font-style: italic; font-weight: 700; font-size: 5.1px; line-height: 6.9px; color: var(--leaf); }

  /* Spine */
  .spine { position: absolute; left: 240px; top: 0; width: 36px; height: 343px; }
  .spine .vertical { position: absolute; transform-origin: 0 0; transform: rotate(90deg); white-space: nowrap; }
  .spine .script { font-size: 22px; left: 30px; top: 14px; }
  .spine .block-title { font-size: 12.6px; letter-spacing: 1.6px; left: 31px; top: 72px; }
  .spine .rule { position: absolute; left: 4px; top: 222px; width: 28px; height: 1.6px; background: var(--berry); }
  .spine .author-spine { left: 22px; top: 233px; font-family: "Montserrat", sans-serif; font-weight: 800; font-size: 7.4px; color: var(--berry); letter-spacing: 0.2px; }

  /* Front cover */
  .front { position: absolute; left: 286px; top: 0; width: 226px; height: 343px; overflow: hidden; }
  .front .script { position: absolute; left: 0; width: 226px; text-align: center; top: 4px; font-size: 44px; }
  .front .block-title { position: absolute; left: 0; width: 226px; text-align: center; top: 68px; font-size: 17px; letter-spacing: 1.8px; }
  .front .stages-lead { position: absolute; left: 0; width: 226px; text-align: center; top: 95px; font-size: 6.4px; font-weight: 700; font-style: italic; }
  .front .stages { position: absolute; left: 0; width: 226px; top: 106px; list-style: none; text-align: center; font-size: 6.4px; line-height: 12.7px; }
  .front .tree-photo {
    position: absolute; left: 6px; top: 184px; width: 214px; height: 159px;
    background:
      radial-gradient(ellipse 60% 55% at 50% 42%, var(--canopy-light) 0%, var(--canopy-dark) 70%, rgba(62,106,28,0) 100%),
      radial-gradient(ellipse 40% 40% at 50% 50%, var(--fruit-warm) 0%, rgba(201,138,44,0) 100%);
    opacity: 0.9;
  }
  .front .author { position: absolute; left: 0; width: 226px; text-align: center; top: 317px; font-size: 12.6px; letter-spacing: 1.2px; z-index: 2; }
</style>
</head>
<body>
<div class="canvas">
  <div class="wrap">

    <section class="back">
      <div class="script">Orchard</div>
      <div class="block-title">BOUGH GROWING</div>
      <div class="byline">BY MARLENE OKAFOR</div>
      <p class="blurb">How to grow a thriving orchard and reap a bountiful harvest in less than a year – in both urban and non-urban settings Fruit trees are fun to grow and will reward you with years of fresh, juicy homegrown produce. However, the process can be excruciating, especially if you don’t know the best varieties to grow or how to control pests and diseases. With a little planning and guidance, you will soon be biting into mellow fruits from trees in your backyard – including cherries, plums, pears, apples, and more. All you need is to learn how to care for the trees, which you will find inside.</p>
      <div class="discover-head">IN ORCHARD BOUGH GROWING, YOU’LL DISCOVER:</div>
      <ul class="points col-a">
        <li>How to pick the right fruit tree varieties for your growing zone and needs to ensure the plants don’t die</li>
        <li>How to effectively plan and prepare the planting site to lay a good foundation for your incoming trees</li>
        <li>How to choose the right irrigation system for your orchard and keep your fruit trees nourished all year long</li>
        <li>Examples of fruit garden plans for different regions – including a guide to help you design your small backyard space</li>
        <li>How to plant fruits to ensure proper pollination, fertilization, and flourishing growth of your produce</li>
      </ul>
      <ul class="points col-b">
        <li>Different fruit tree propagation methods with step-by-step instructions to help you grow your trees without spending money on costly grafts</li>
        <li>When and how to harvest fruits to ensure you collect them at their best and prevent wasting your hard work</li>
        <li>How to boost fruit production, encourage growth, and protect your trees from dangerous diseases</li>
        <li>How to look after fruit trees during all seasons, practice organic farming, and control pests in your garden</li>
        <li class="tail">And much more…</li>
      </ul>
      <p class="closing">IT’S TIME TO GROW YOUR MINI-ORCHARD AND BASK IN YEARS OF HARVEST AND SWEETNESS FROM YOUR LABOR. DISCOVER HOW YOU CAN HAVE A THRIVING ORCHARD AND A BOUNTIFUL FRUIT HARVEST.</p>
    </section>

    <section class="spine">
      <div class="vertical script">Orchard</div>
      <div class="vertical block-title">BOUGH GROWING</div>
      <div class="rule"></div>
      <div class="vertical author-spine">MARLENE OKAFOR</div>
    </section>

    <section class="front">
      <div class="script">Orchard</div>
      <div class="block-title">BOUGH GROWING</div>
      <div class="stages-lead">7 EASY STAGES COVERING</div>
      <ul class="stages">
        <li>GROUND CHOICE</li>
        <li>BLOSSOM CARE AND FEEDING</li>
        <li>TRIMMING</li>
        <li>TINY PLOTS</li>
        <li>BUG MANAGEMENT</li>
        <li>EXOTIC ORCHARD PLANTS, AND VINES</li>
      </ul>
      <div class="tree-photo" role="img" aria-label="Photograph of a leafy orange tree heavy with ripe fruit"></div>
      <div class="author">MARLENE OKAFOR</div>
    </section>

  </div>
</div>
</body>
</html>
```